Bref créative
Business Card for Real Estate Company
Larkfield Residences
Professional
Marcy Dunwell
Realtor
248 E. Corwin Ave. Suite 716
Anchorage, Alaska 40817
larkfieldtx@mailvista.example
www.larkfieldtx.example
Its a card for a Norcott Praine Realtor. Make sure in small print somewhere on card its states "Each Office Independently Owned and Operated"

```html
<!DOCTYPE html>
<html lang="en">
<head>
<meta charset="utf-8">
<title>Larkfield Residences – Business Card</title>
<link rel="stylesheet" href="https://fonts.googleapis.com/css2?family=Open+Sans:ital,wght@0,400;0,600;0,700;1,700&family=Raleway:wght@600&display=swap">
<style>
  :root {
    --bg: #e9e7e4;
    --card: #ffffff;
    --brand-red: #a8182a;
    --band-red: #a01c2b;
    --swoosh-gray: #b9b9bb;
    --ink: #3a3a3a;
    --light: #ffffff;
  }
  * { box-sizing: border-box; margin: 0; padding: 0; }
  html, body { width: 1200px; height: 988px; overflow: hidden; background: var(--bg); }
  body { position: relative; font-family: "Open Sans", sans-serif; }

  .card {
    position: absolute; left: 220px; width: 760px; height: 434px;
    background: var(--card); box-shadow: 0 6px 18px rgba(0,0,0,.18); overflow: hidden;
  }
  .card--back { top: 40px; }
  .card--front { top: 514px; }

  .brand-name {
    font-family: "Raleway", sans-serif; font-weight: 600; color: var(--brand-red);
    letter-spacing: 3px; text-transform: uppercase; display: flex; align-items: center; gap: 12px;
  }
  .brand-name .mark { width: 14px; height: 14px; background: var(--brand-red); }

  .card--back .brand-name {
    position: absolute; top: 150px; left: 0; right: 0; justify-content: center; font-size: 34px;
  }
  .tagline {
    position: absolute; top: 225px; left: 0; right: 0; text-align: center;
    font-style: italic; font-weight: 700; font-size: 19px; color: var(--ink);
  }

  .card--front .waves { position: absolute; inset: 0; }
  .card--front .brand-name {
    position: absolute; top: 95px; left: 260px; font-size: 26px;
  }
  .agent { position: absolute; left: 420px; top: 250px; color: var(--light); }
  .agent-name { font-weight: 700; font-size: 15px; }
  .agent-title { font-size: 11px; margin-top: 1px; }

  .office {
    position: absolute; left: 150px; top: 330px; color: var(--light);
    font-size: 10.5px; line-height: 1.55;
  }
  .contact-list {
    position: absolute; left: 420px; top: 298px; list-style: none; color: var(--light);
    font-size: 10.5px; line-height: 1;
  }
  .contact-list li { display: flex; align-items: center; gap: 7px; margin-bottom: 6px; }
  .contact-list svg { width: 12px; height: 12px; flex: none; }
</style>
</head>
<body>

<section class="card card--back" aria-label="Card back">
  <div class="brand-name"><span class="mark"></span>Larkfield Residences</div>
  <p class="tagline">"Each Office independently owned and operated"</p>
</section>

<section class="card card--front" aria-label="Card front">
  <svg class="waves" viewBox="0 0 760 434" preserveAspectRatio="none" aria-hidden="true">
    <path d="M0,205 C230,180 470,145 760,128 L760,160 C480,168 240,200 0,232 Z" fill="var(--swoosh-gray)"/>
    <path d="M0,232 C240,205 480,172 760,166 L760,434 L0,434 Z" fill="var(--band-red)"/>
  </svg>

  <div class="brand-name"><span class="mark"></span>Larkfield Residences</div>

  <div class="agent">
    <p class="agent-name">Marcy Dunwell</p>
    <p class="agent-title">Realtor</p>
  </div>

  <address class="office" style="font-style:normal">
    Norcott Praine Realty, Alaska Group<br>
    248 E. Corwin Ave. Suite 716<br>
    Anchorage, Alaska 40817
  </address>

  <ul class="contact-list">
    <li><svg viewBox="0 0 12 12"><circle cx="6" cy="6" r="6" fill="#fff"/><path d="M4 3.2l1 1-.6.8c.4.9 1 1.5 1.9 1.9l.8-.6 1 1-.7.9C5.6 8 4 6.4 3.1 3.9z" fill="var(--band-red)"/></svg>(907) 555-0143</li>
    <li><svg viewBox="0 0 12 12"><circle cx="6" cy="6" r="6" fill="#fff"/><rect x="4.2" y="2.8" width="3.6" height="6.4" rx=".6" fill="var(--band-red)"/></svg>(907) 555-0178</li>
    <li><svg viewBox="0 0 12 12"><circle cx="6" cy="6" r="6" fill="#fff"/><rect x="3" y="4.5" width="6" height="3.5" fill="var(--band-red)"/></svg>(907) 555-0192</li>
    <li><svg viewBox="0 0 12 12"><circle cx="6" cy="6" r="6" fill="#fff"/><rect x="3" y="4" width="6" height="4" fill="var(--band-red)"/><path d="M3 4l3 2.2L9 4" stroke="#fff" stroke-width=".7" fill="none"/></svg>larkfieldtx@mailvista.example</li>
    <li><svg viewBox="0 0 12 12"><circle cx="6" cy="6" r="6" fill="#fff"/><circle cx="6" cy="6" r="3" fill="none" stroke="var(--band-red)" stroke-width="1"/><path d="M3 6h6M6 3v6" stroke="var(--band-red)" stroke-width=".7"/></svg>www.larkfieldtx.example</li>
  </ul>
</section>

</body>
</html>
```